Childcare Stationery( business cards, letter head, envelopes and letter size folders)
Pebble Early Education Center
Modern
Danvir Okonkwo-Hale
287 West Birch Avenue
Columbus, Ohio 43215
danvirok@pebble2learn.com
www.pebble2learn.com
Nurture, Flourish, Grow
Please use logo and colors.

```html
<!DOCTYPE html>
<html lang="en">
<head>
<meta charset="utf-8">
<title>Pebble Early Education Center – Business Cards</title>
<link href="https://fonts.googleapis.com/css2?family=PT+Sans:wght@400;700&display=swap" rel="stylesheet">
<style>
  :root {
    --bg: #d9d9d9;
    --label: #222222;
    --white: #ffffff;
    --green: #6cbd45;
    --green-dark: #4f9e2f;
    --leaf-soft: #8ccc5e;
    --blue: #2bb5e8;
    --ink: #1d2a33;
    --grey-text: #555555;
  }
  * { box-sizing: border-box; margin: 0; padding: 0; }
  html, body { width: 1200px; height: 826px; overflow: hidden; }
  body {
    background: var(--bg);
    font-family: "PT Sans", Arial, sans-serif;
    position: relative;
  }
  .side-label {
    position: absolute;
    font-size: 28px;
    line-height: 1;
    color: var(--label);
    transform: translateX(-50%);
  }
  .card {
    position: absolute;
    border-radius: 22px;
    overflow: hidden;
    box-shadow: 0 6px 14px rgba(0,0,0,0.25);
  }
  /* Front */
  .card-front {
    left: 336px; top: 94px;
    width: 545px; height: 300px;
    background: var(--white);
  }
  .holder-name {
    position: absolute; left: 26px; top: 28px;
    font-size: 19px; font-weight: 700; color: var(--green-dark);
  }
  .holder-phone {
    position: absolute; left: 26px; top: 62px;
    font-size: 11px; color: var(--grey-text);
  }
  .leaf-art {
    position: absolute; left: -30px; top: 118px;
    width: 230px; height: 230px;
    background: linear-gradient(135deg, var(--leaf-soft), var(--green));
    border-radius: 0 100% 0 100%;
  }
  .license {
    position: absolute; left: 66px; top: 238px;
    font-size: 11px; line-height: 1.25; color: var(--white);
  }
  .brand-dot {
    position: absolute; left: 382px; top: 24px;
    width: 40px; height: 40px; border-radius: 50%;
    background: var(--green);
  }
  .brand-name {
    position: absolute; left: 268px; top: 88px; width: 258px;
    text-align: center;
    font-size: 28px; line-height: 1.1; font-weight: 700;
    color: var(--blue);
  }
  .contact {
    position: absolute; left: 208px; top: 240px;
    font-size: 11px; line-height: 22px; color: var(--grey-text);
    white-space: nowrap;
  }
  /* Backs */
  .card-back { top: 474px; width: 540px; height: 314px; }
  .card-back.blue-back { left: 29px; background: var(--blue); }
  .card-back.green-back { left: 631px; background: var(--green); }
  .tagline {
    position: absolute; left: 0; right: 0; top: 28px;
    text-align: center; font-size: 22px; color: var(--ink);
  }
  .url-band {
    position: absolute; left: 0; right: 0; bottom: 0;
    display: flex; align-items: center; justify-content: center;
    font-size: 15px; color: var(--white); letter-spacing: 0.5px;
  }
  .blue-back .url-band { background: var(--green); height: 50px; }
  .green-back .url-band { background: var(--blue); height: 50px; }
</style>
</head>
<body>
  <div class="side-label" style="left:608px; top:52px;">Front</div>
  <div class="side-label" style="left:293px; top:418px;">Back - 1</div>
  <div class="side-label" style="left:902px; top:418px;">Back - 2</div>

  <section class="card card-front">
    <div class="holder-name">Danvir Okonkwo-Hale</div>
    <div class="holder-phone">T: 614-555-0148</div>
    <div class="leaf-art" role="img" aria-label="Large green leaf illustration"></div>
    <div class="license">License No<br>00000 00000</div>
    <div class="brand-dot"></div>
    <div class="brand-name">Pebble Early Education Center</div>
    <div class="contact">
      danvirok@pebble2learn.com &nbsp; www.pebble2learn.com<br>
      287 West Birch Avenue, Columbus, Ohio 43215
    </div>
  </section>

  <section class="card card-back blue-back">
    <div class="tagline">Nurture. Flourish. Grow</div>
    <div class="url-band">www.pebble2learn.com</div>
  </section>

  <section class="card card-back green-back">
    <div class="tagline">Nurture. Flourish. Grow</div>
    <div class="url-band">www.pebble2learn.com</div>
  </section>
</body>
</html>
```